Kettle Ledger Business Card design

We need a stand out business card design for Accounting practice based in Australia specialising in pubs, clubs and hotels. We help venues maximise margins, create time and manage cashflow. One club we have been working with for the last 6 months has increased revenue by 3% and margin by 5% in this time frame. We have a back office outsourced system that costs less than having a full time employee and also allows the venues the added benefit of:<br/>-using the office space to become a revenue generating opportunity. <br/>-a complete system to enhance governance, accountability and efficiency within their operation<br/>-52 weeks cover so no hassle to cover annual/sick .. leave<br/><br/>We would like to see designs that use the colours of our logo (green & blue).
Target Market(s)
Australian Pubs, Clubs & Hotels abookkeeping, accounting and tax services
Industry/Entity Type
Accountant
Contact Information for Business Card
Miriam Oakley CPA
Principal
Accountant Tax Agent
Miriam@KettleLedger-example.com.au
0418693142
www.kettleledger-example.com.au
Accounting / Payroll / Tax / SMSF / Technology
Colors
Designer to choose colors to be used in the design.
Look and feel
Each slider illustrates characteristics of the customer's brand and the style your logo design should communicate.

```html
<!DOCTYPE html>
<html lang="en">
<head>
<meta charset="utf-8">
<title>Kettle Ledger Business Card</title>
<link rel="stylesheet" href="https://fonts.googleapis.com/css2?family=Open+Sans:wght@400;700&family=Poppins:wght@700&display=swap">
<style>
  :root {
    --page-bg: #e9e9e6;
    --brand-blue: #24418f;
    --brand-green: #07723c;
    --seal-white: #f3f3f3;
    --text-light: #ffffff;
  }
  html, body {
    margin: 0;
    width: 1200px;
    height: 900px;
    overflow: hidden;
    background: var(--page-bg);
  }
  .business-card {
    position: absolute;
    left: 120px;
    top: 152px;
    width: 960px;
    height: 595px;
    background: var(--brand-blue);
    overflow: hidden;
    font-family: "Open Sans", Arial, sans-serif;
    color: var(--text-light);
    box-shadow: 0 10px 30px rgba(0,0,0,0.18);
  }
  .green-band {
    position: absolute;
    top: 0;
    right: 0;
    width: 310px;
    height: 100%;
    background: var(--brand-green);
  }
  .brand-seal {
    position: absolute;
    left: 394px;
    top: 25px;
    width: 516px;
    height: 516px;
    border-radius: 50%;
    background: var(--seal-white);
    display: flex;
    align-items: center;
    justify-content: center;
    gap: 18px;
  }
  .brand-dot {
    width: 58px;
    height: 58px;
    border-radius: 50%;
    background: var(--brand-green);
  }
  .brand-name {
    font-family: "Open Sans", Arial, sans-serif;
    font-weight: 700;
    font-size: 50px;
    line-height: 1;
    color: var(--brand-blue);
  }
  .holder {
    position: absolute;
    left: 44px;
    top: 70px;
  }
  .holder-name {
    margin: 0;
    font-weight: 700;
    font-size: 33px;
    letter-spacing: 0.5px;
    line-height: 1.1;
  }
  .holder-role {
    margin: 6px 0 0;
    font-size: 23px;
    line-height: 1.4;
  }
  .contact-list {
    position: absolute;
    left: 44px;
    top: 410px;
    margin: 0;
    padding: 0;
    list-style: none;
    font-size: 22px;
  }
  .contact-list li {
    display: flex;
    align-items: center;
    gap: 8px;
    height: 35px;
  }
  .contact-icon {
    width: 26px;
    height: 26px;
    flex: none;
  }
</style>
</head>
<body>
  <div class="business-card">
    <div class="green-band"></div>

    <div class="brand-seal">
      <span class="brand-dot"></span>
      <span class="brand-name">Kettle Ledger</span>
    </div>

    <div class="holder">
      <h1 class="holder-name">MIRIAM OAKLEY CPA</h1>
      <p class="holder-role">Principal<br>Accountant Tax Agent</p>
    </div>

    <ul class="contact-list">
      <li>
        <svg class="contact-icon" viewBox="0 0 24 24" aria-hidden="true">
          <rect x="2" y="2" width="20" height="20" rx="4" fill="none" stroke="#fff" stroke-width="2"/>
          <path d="M8 6.5c-1 .5-1.5 1.5-1 3 1 3 3.5 5.5 6.5 7 1.5.5 2.5 0 3-1l-2-2-1.5 1c-1.5-.8-2.7-2-3.5-3.5l1-1.5z" fill="#fff"/>
        </svg>
        <span>0418693142</span>
      </li>
      <li>
        <svg class="contact-icon" viewBox="0 0 24 24" aria-hidden="true">
          <rect x="1.5" y="5" width="21" height="14" fill="#fff"/>
          <path d="M1.5 5l10.5 8 10.5-8" fill="none" stroke="#24418f" stroke-width="1.6"/>
        </svg>
        <span>www.kettleledger-example.com.au</span>
      </li>
      <li>
        <svg class="contact-icon" viewBox="0 0 24 24" aria-hidden="true">
          <circle cx="12" cy="12" r="10.5" fill="#fff"/>
          <g fill="none" stroke="#24418f" stroke-width="1.3">
            <ellipse cx="12" cy="12" rx="4.5" ry="10.5"/>
            <line x1="1.5" y1="12" x2="22.5" y2="12"/>
            <path d="M3.5 7h17M3.5 17h17"/>
          </g>
        </svg>
        <span>Miriam@KettleLedger-example.com.au</span>
      </li>
    </ul>
  </div>
</body>
</html>
```